Brill's Jewelers website (www.brillsjewelers-example.com)

We are in need of a web storefront for a retail Jewelry store.
www.brillsjewelers-example.com
https://www.facebook.com/Brills-Jewelers-Palm-Vista-740315928461257/

Brill's Jewelers is located in Coral Gables, Florida. The store has been family owned and operated since 1958. Their focus customers are high-income families that care about quality over the brand name. They mostly sell fashion jewelry and diamonds up to 8 carats. We are looking for a simple minimalistic site that their customers can view their inventory and purchase items online.

Competitors websites:
https://www.orvinjewelers-example.com/
http://www.pelvaro-example.com/
http://truecutjewelers-example.com/

Pages:
-Home (with message bulletin)
-Jewelry
We would be able to create the subpages ie Rings, Bracelets, Earrings, Necklaces, Estate, Watches, Men's, Children's
-Services
We would need sub pages ie Appraisals, Consignment, Repairs
-About us
-Contact

Target Market(s)

Local wealthy families

Coding

Number of Pages Required

Font styles to use
Serif

Requirements
Must have
• -An E-commerce site customers can buy jewelry online.
-An easy process internally to add new items to the site
-Colors are Black and White or Black and Gold
Nice to have
• I would like to stay away from face shots of random models in stock photos. I want the jewelry pieces as the focus, not models.

```html
<!DOCTYPE html>
<html lang="en">
<head>
<meta charset="utf-8">
<title>Brill's Jewelry — Storefront Screens</title>
<link rel="stylesheet" href="https://fonts.googleapis.com/css2?family=Cormorant+Garamond:wght@400;500&family=Jost:wght@400;500&display=swap">
<style>
  :root {
    --backdrop-light: #c2a68c;
    --backdrop-dark: #8f7560;
    --stone: #b08f73;
    --stone-deep: #a4836a;
    --cream: #f5ede4;
    --ivory: #fcf9f5;
    --ink: #2a2522;
    --muted: #b5aaa1;
    --accent: #e2571c;
    --white: #ffffff;
    --rule: #3a3430;
    --serif: "Cormorant Garamond", serif;
    --sans: "Jost", sans-serif;
  }
  * { box-sizing: border-box; margin: 0; padding: 0; }
  html, body { width: 1200px; height: 2736px; overflow: hidden; }
  body {
    position: relative;
    background: radial-gradient(ellipse at 30% 20%, var(--backdrop-light), var(--backdrop-dark) 90%);
    font-family: var(--sans);
    color: var(--ink);
  }
  .screen {
    position: absolute;
    left: 79px;
    width: 1042px;
    height: 587px;
    overflow: hidden;
    box-shadow: 0 10px 22px rgba(40, 25, 15, 0.35);
  }
  .abs { position: absolute; }
  .photo { position: absolute; }

  /* ---------- Hero ---------- */
  .hero { top: 78px; background: linear-gradient(135deg, var(--stone), var(--stone-deep)); }
  .hero-photo {
    left: 553px; top: 0; width: 489px; height: 587px;
    background: linear-gradient(160deg, #9a9a86 0%, #7b7462 40%, #5a4c43 75%, #6d6a52 100%);
  }
  .menu-icon { position: absolute; width: 30px; height: 8px; }
  .menu-icon::before, .menu-icon::after {
    content: ""; position: absolute; left: 0; width: 100%; height: 1px; background: currentColor;
  }
  .menu-icon::before { top: 0; } .menu-icon::after { bottom: 0; }
  .hero .menu-icon { left: 31px; top: 29px; color: var(--white); }
  .wordmark { position: absolute; font-family: var(--serif); font-weight: 400; white-space: nowrap; letter-spacing: 0.5px; }
  .hero .wordmark { left: 208px; top: 19px; font-size: 20px; color: var(--white); }
  .hero-headline {
    position: absolute; left: 80px; top: 112px;
    font-family: var(--serif); font-weight: 400; font-size: 82px; line-height: 96px;
    color: var(--white); letter-spacing: 1px; white-space: nowrap;
  }
  .hero-subline {
    position: absolute; left: 302px; top: 412px;
    font-family: var(--serif); font-size: 52px; color: var(--white); white-space: nowrap; letter-spacing: 1px;
  }
  .hero-note {
    position: absolute; right: 29px; top: 25px; text-align: right;
    font-size: 10.5px; line-height: 13.8px; color: var(--white); font-weight: 500;
  }
  .collections-link {
    position: absolute; left: 363px; top: 341px;
    font-family: var(--serif); font-size: 13px; color: var(--white); text-decoration: underline;
  }
  .hero-svg { position: absolute; left: 0; top: 0; }
  .featured-piece {
    left: 30px; top: 405px; width: 70px; height: 64px; border-radius: 50%;
    background: radial-gradient(circle, #f4f4f4, #bfc2c4 60%, rgba(190,190,190,0) 72%);
  }

  /* ---------- Categories ---------- */
  .categories { top: 741px; background: var(--cream); }
  .category-row {
    position: absolute; display: flex; align-items: flex-start; white-space: nowrap;
    font-family: var(--serif); font-size: 90px; line-height: 1; color: var(--muted);
    z-index: 2;
  }
  .category-row.is-active { color: var(--accent); }
  .category-count {
    margin-left: 24px; margin-top: 8px; font-family: var(--sans); font-size: 15px; line-height: 1;
  }
  .category-slash { width: 30px; height: 72px; margin-left: -8px; margin-top: 4px; }
  .category-photo-left {
    left: 79px; top: 289px; width: 331px; height: 220px; z-index: 1;
    background: radial-gradient(ellipse at 60% 45%, #e8cfc6, #b8918a 55%, #8f7370 100%);
  }
  .category-photo-right {
    left: 760px; top: 220px; width: 204px; height: 136px; z-index: 1;
    background: linear-gradient(135deg, #6f7a58, #b7b69f 50%, #e4e2da 80%);
  }

  /* ---------- Shared page header ---------- */
  .page-header .menu-icon { left: 30px; top: 30px; color: var(--ink); }
  .page-header .wordmark { left: 0; width: 1042px; text-align: center; top: 16px; font-size: 22px; color: var(--ink); }
  .account-links {
    position: absolute; right: 33px; top: 30px; text-align: right;
    font-size: 10.5px; line-height: 14px;
  }
  .account-links .count { color: var(--accent); }
  .breadcrumb {
    position: absolute; left: 30px; top: 70px; display: flex; gap: 14px; align-items: center;
    font-size: 7px;
  }
  .breadcrumb .sep { width: 3px; height: 3px; border-radius: 50%; background: var(--accent); }

  /* ---------- Listing ---------- */
  .listing { top: 1406px; background: var(--cream); }
  .listing-title {
    position: absolute; left: 201px; top: 98px;
    font-family: var(--serif); font-size: 92px; line-height: 1; color: var(--accent);
  }
  .filters { position: absolute; top: 166px; font-size: 7px; font-weight: 500; }
  .filters span::after {
    content: ""; display: inline-block; width: 3px; height: 3px; border-radius: 50%;
    background: var(--accent); margin-left: 3px; vertical-align: middle;
  }
  .sidebar { position: absolute; left: 30px; top: 226px; width: 125px; }
  .sidebar-rule { position: absolute; left: 0; width: 125px; height: 1px; background: var(--rule); }
  .sidebar-item { position: absolute; left: 0; font-size: 11px; white-space: nowrap; }
  .sidebar-heading { position: absolute; left: 0; font-size: 18px; }
  .sidebar-sub { position: absolute; left: 0; font-size: 6.5px; line-height: 16px; }
  .product-card { position: absolute; width: 243px; height: 242px; background: var(--white); }
  .product-label { position: absolute; left: 15px; top: 14px; font-size: 11px; }
  .product-price {
    position: absolute; right: 11px; top: 9px;
    font-family: var(--serif); font-size: 18px; color: var(--accent);
  }
  .product-shot {
    position: absolute; left: 71px; top: 60px; width: 100px; height: 100px; border-radius: 50%;
    background: radial-gradient(circle, #f6f6f6, #cfd1d3 45%, rgba(255,255,255,0) 70%);
  }

  /* ---------- Product ---------- */
  .product { top: 2071px; background: var(--ivory); }
  .product-name {
    position: absolute; left: 51px; top: 145px;
    font-family: var(--serif); font-size: 36px; font-weight: 500;
  }
  .product-cost { position: absolute; left: 51px; top: 214px; font-size: 10.5px; color: var(--accent); }
  .perks { position: absolute; left: 53px; top: 266px; list-style: none; font-size: 10.5px; }
  .perks li { position: relative; padding-left: 20px; height: 28px; }
  .perks li::before {
    content: ""; position: absolute; left: 0; top: 5px; width: 4px; height: 4px; border-radius: 50%;
    background: var(--accent);
  }
  .perks a { color: inherit; text-decoration: none; border-bottom: 1px solid var(--accent); }
  .product-photo {
    left: 416px; top: 131px; width: 248px; height: 223px; border-radius: 50%;
    background: radial-gradient(ellipse at 50% 40%, #ffffff, #dcdee0 40%, #a8acaf 62%, rgba(252,249,245,0) 72%);
  }
  .materials { position: absolute; left: 785px; top: 213px; width: 210px; }
  .materials h2 { font-family: var(--sans); font-weight: 500; font-size: 17px; margin-bottom: 14px; }
  .materials h3 { font-weight: 400; font-size: 10.5px; margin-bottom: 10px; }
  .materials p { font-size: 10.5px; line-height: 13.5px; }
  .add-to-cart {
    position: absolute; left: 785px; top: 374px;
    font-family: var(--serif); font-weight: 500; font-size: 13px; color: var(--accent);
  }
  .pager-label { position: absolute; top: 475px; font-size: 10.5px; color: var(--accent); }
</style>
</head>
<body>

<!-- Hero -->
<section class="screen hero">
  <div class="photo hero-photo" role="img" aria-label="Two gold wedding bands hanging on a blossoming cherry branch"></div>
  <span class="menu-icon"></span>
  <div class="wordmark">Brill's Jewelry</div>
  <p class="hero-note">You have trusted us<br>for decades with your<br>fine jewelry, custom designs,<br>and repairs.<br>Now come in and see<br>what's in store.</p>
  <h1 class="hero-headline">YOUR HOMETOWN<br>JEWELER</h1>

  <svg class="hero-svg" width="1042" height="587" viewBox="0 0 1042 587" aria-hidden="true">
    <g fill="none" stroke="#ffffff" stroke-width="1">
      <circle cx="49" cy="439" r="103"/>
      <polyline points="49,316 55,310 61,316"/>
      <polyline points="49,561 55,567 61,561"/>
      <polyline points="836,501 875,539 914,501"/>
    </g>
    <g fill="#ffffff">
      <circle cx="161" cy="378" r="2.5" opacity="0.7"/>
      <circle cx="174" cy="406" r="2.5" opacity="0.7"/>
      <circle cx="184" cy="437" r="4.5"/>
      <circle cx="174" cy="465" r="2.5" opacity="0.7"/>
      <circle cx="161" cy="495" r="2.5" opacity="0.7"/>
    </g>
  </svg>
  <div class="photo featured-piece" role="img" aria-label="Diamond halo engagement ring"></div>
  <a class="collections-link">View New Collections</a>
  <p class="hero-subline">JUST GOT A NEW HOME</p>
</section>

<!-- Categories -->
<section class="screen categories">
  <div class="photo category-photo-left" role="img" aria-label="Rose-toned gemstone ring resting on sparkling jewelry"></div>
  <div class="photo category-photo-right" role="img" aria-label="Gold wedding bands on a flowering branch"></div>

  <div class="category-row is-active" style="left:431px; top:24px;">
    <span>Rings</span><span class="category-count">34</span>
    <svg class="category-slash" viewBox="0 0 30 72" aria-hidden="true"><line x1="28" y1="2" x2="4" y2="70" stroke="currentColor" stroke-width="1.2"/></svg>
  </div>
  <div class="category-row" style="left:399px; top:135px;">
    <span>Bracelets</span><span class="category-count">21</span>
    <svg class="category-slash" viewBox="0 0 30 72" aria-hidden="true"><line x1="28" y1="2" x2="4" y2="70" stroke="currentColor" stroke-width="1.2"/></svg>
  </div>
  <div class="category-row" style="left:339px; top:246px;">
    <span>Earrings</span><span class="category-count">11</span>
    <svg class="category-slash" viewBox="0 0 30 72" aria-hidden="true"><line x1="28" y1="2" x2="4" y2="70" stroke="currentColor" stroke-width="1.2"/></svg>
  </div>
  <div class="category-row" style="left:421px; top:357px;">
    <span>Necklaces</span><span class="category-count">31</span>
    <svg class="category-slash" viewBox="0 0 30 72" aria-hidden="true"><line x1="28" y1="2" x2="4" y2="70" stroke="currentColor" stroke-width="1.2"/></svg>
  </div>
  <div class="category-row" style="left:339px; top:467px;">
    <span>Watches</span><span class="category-count">27</span>
    <svg class="category-slash" viewBox="0 0 30 72" aria-hidden="true"><line x1="28" y1="2" x2="4" y2="70" stroke="currentColor" stroke-width="1.2"/></svg>
  </div>
</section>

<!-- Listing -->
<section class="screen listing page-header">
  <span class="menu-icon"></span>
  <div class="wordmark">Brill's Jewelry</div>
  <div class="account-links">cart (<span class="count">1</span>)<br>account</div>
  <nav class="breadcrumb"><span>main page</span><span class="sep"></span><span>jewerly</span><span class="sep"></span><span>earrings</span></nav>

  <h1 class="listing-title">Earrings</h1>
  <div class="filters" style="left:797px;"><span>Size</span></div>
  <div class="filters" style="left:849px;"><span>Brand</span></div>
  <div class="filters" style="left:912px;"><span>Collection</span></div>

  <aside class="sidebar">
    <span class="sidebar-rule" style="top:0;"></span>
    <span class="sidebar-item" style="top:12px;">Shop all</span>
    <span class="sidebar-rule" style="top:40px;"></span>
    <span class="sidebar-heading" style="top:50px;">Earrings</span>
    <div class="sidebar-sub" style="top:80px;">Single Hoops<br>Hoops<br>Studs<br>Earrings<br>Ear cuffs<br>Chain earrings + threaders</div>
    <span class="sidebar-rule" style="top:188px;"></span>
    <span class="sidebar-item" style="top:202px;">Necklaces</span>
    <span class="sidebar-rule" style="top:229px;"></span>
    <span class="sidebar-item" style="top:241px;">Rings</span>
    <span class="sidebar-rule" style="top:269px;"></span>
    <span class="sidebar-item" style="top:281px;">Bracelets + Anklets</span>
    <span class="sidebar-rule" style="top:307px;"></span>
    <span class="sidebar-item" style="top:320px;">Engagement</span>
    <span class="sidebar-rule" style="top:343px;"></span>
  </aside>

  <article class="product-card" style="left:207px; top:227px;">
    <span class="product-label">Earrings</span><span class="product-price">55$</span>
    <div class="product-shot" role="img" aria-label="Diamond flower drop earrings"></div>
  </article>
  <article class="product-card" style="left:457px; top:227px;">
    <span class="product-label">Earrings</span><span class="product-price">55$</span>
    <div class="product-shot" role="img" aria-label="Pearl and diamond stud earrings"></div>
  </article>
  <article class="product-card" style="left:707px; top:227px;">
    <span class="product-label">Earrings</span><span class="product-price">55$</span>
    <div class="product-shot" role="img" aria-label="Diamond stud earrings"></div>
  </article>
  <article class="product-card" style="left:207px; top:478px;">
    <span class="product-label">Earrings</span><span class="product-price">55$</span>
    <div class="product-shot" role="img" aria-label="Pearl stud earring"></div>
  </article>
  <article class="product-card" style="left:457px; top:478px;">
    <span class="product-label">Earrings</span><span class="product-price">55$</span>
    <div class="product-shot" role="img" aria-label="Pearl stud earring"></div>
  </article>
  <article class="product-card" style="left:707px; top:478px;">
    <span class="product-label">Earrings</span><span class="product-price">55$</span>
    <div class="product-shot" role="img" aria-label="Pearl stud earring"></div>
  </article>
</section>

<!-- Product -->
<section class="screen product page-header">
  <span class="menu-icon"></span>
  <div class="wordmark">Brill's Jewelry</div>
  <div class="account-links">cart (<span class="count">1</span>)<br>account</div>
  <nav class="breadcrumb"><span>main page</span><span class="sep"></span><span>jewerly</span><span class="sep"></span><span>diamond ring</span></nav>

  <h1 class="product-name">Diamond Ring</h1>
  <p class="product-cost">65$</p>
  <ul class="perks">
    <li>Free Expedited Shipping Over $150+</li>
    <li>Extended Holiday Returns. <a>Learn more</a></li>
    <li>2 Year Warranty</li>
  </ul>

  <div class="photo product-photo" role="img" aria-label="Diamond halo engagement ring with pavé band"></div>

  <div class="materials">
    <h2>Materials</h2>
    <h3>Lorem</h3>
    <p>Lorem ipsum dolor sit amet,<br>consectetur adipiscing elit,<br>sed do eiusmod tempor incididunt<br>ut labore et dolore magna aliqua.<br>Eu tincidunt tortor aliquam nulla facilisi.</p>
  </div>
  <a class="add-to-cart">Add To Cart</a>

  <svg class="abs" style="left:0; top:0;" width="1042" height="587" viewBox="0 0 1042 587" aria-hidden="true">
    <g fill="none" stroke-width="1">
      <line x1="48" y1="482" x2="439" y2="482" stroke="#6b625c"/>
      <line x1="604" y1="482" x2="994" y2="482" stroke="#6b625c"/>
      <circle cx="521" cy="482" r="34" stroke="#e2571c"/>
      <line x1="547" y1="431" x2="498" y2="533" stroke="#e2571c"/>
    </g>
  </svg>
  <span class="pager-label" style="left:452px;">Next</span>
  <span class="pager-label" style="left:568px;">Prev</span>
</section>

</body>
</html>
```